Riverbend Trusted Home Care-Flyer for Patients

Our Home Health Care Agency, Riverbend Trusted Home Care, is seeking a flyer to advertise our services. We would like our flyer to convey professionalism, classiness and sophistication. We want our agency to come across as one that is well-established and recognized as being first-rate within the field.

We also want to appear original; we want to stand out.

Our theme colors, blue and green, from our logo should be incorporated into the flyer's design (refer below).

The top of the page should say (in a clear, bold font)-Seeking Care for your Loved One?

Our Logo, followed by our slogan, "Lean On Those Nearby", should be in the center. (This should make it appear as if our agency is the obvious solution to the consumer's quest in finding suitable care for their family member). This should be in a big font.
Below that, our agency's services should be listed in a very noticeable font...yet smaller than what's written above that.
The text should read:
Our Services Include:
*Experienced Certified Home Health Aides/ Live In Home Health Aides/Companions
*Nursing Services
*Alzheimer’s and Dementia Care
*Respite Care
*Postoperative Care
*Post Rehabilitation Care
*Running Errands
*Light Housekeeping
*Assistance with Bathing, Feeding and Grooming
*Meal Preparation
*Laundry and Linen Washing
*Mail and Bill Organization
*Medication Management
*Accompanying to Doctor’s Appointments
*And much more!
Below that, in a smaller, yet noticeable font:
As seasoned professionals, we know how to help our clients navigate and fulfill their various health care needs. Those nearby are here to help you get the attention that you merit.
Call Riverbend Trusted Home Care today to learn more about our first-rate services!
Below that, in a larger font, our phone number, website, our e-mail address.
*Out contact information will be provided to the project’s winner*.

*Pictures of Caregivers helping elderly patient should be included in the advertisement as well. *

We provided advertisements of other Home Health Care Agencies attached below to use as a reference. Once again, while we are aiming for a similar idea; however, our goal is to stand out as the community's premiere home health care agency, the one that they want to choose. We want to be original as well!

Size: Standard Computer Paper Size. 8.5” x 11”.

Feel free to utilize your creative, designer flair!
We look forward to seeing the results!
Good luck!

Industry/Entity Type

Home Health Care

Font styles to use
Sans Serif

Requirements
Must have
• Refer above.
Nice to have
• Refer to attachment below to see how other home health care agencies advertise. While we are aiming for a similar idea, we would like to incorporate our logo, slogan and colors to make this flyer more unique and stand out. We would like to appear original.

```html
<!DOCTYPE html>
<html lang="en">
<head>
<meta charset="utf-8">
<title>Riverbend Trusted Home Care – Services Flyer</title>
<link href="https://fonts.googleapis.com/css2?family=Roboto:ital,wght@0,300;0,400;0,700;1,300&display=swap" rel="stylesheet">
<style>
  :root{
    --navy:#0b4f98;
    --teal:#008479;
    --blue:#0a4d93;
    --green:#8dc63f;
    --grey-edge:#a9abb0;
    --text-grey:#8a8d92;
    --page-bg:#d6d7d9;
    --white:#ffffff;
  }
  *{box-sizing:border-box;margin:0;padding:0}
  html,body{width:1200px;height:900px;overflow:hidden}
  body{background:var(--page-bg);font-family:'Roboto',Arial,sans-serif;position:relative}
  .flyer{position:absolute;left:270px;top:23px;width:660px;height:854px;background:var(--white);overflow:hidden}
  .flyer-shapes{position:absolute;left:0;top:0;width:660px;height:854px}
  .headline{position:absolute;top:34px;left:0;width:660px;text-align:center;color:var(--navy);font-weight:700;font-size:34px;letter-spacing:-.3px;line-height:1}
  .slogan{position:absolute;top:68px;left:0;width:660px;text-align:center;color:#55585d;font-weight:300;font-style:italic;font-size:34px;line-height:1}
  .brand{position:absolute;top:122px;left:0;width:660px;display:flex;flex-direction:column;align-items:center;gap:10px}
  .brand-mark{width:62px;height:62px;border-radius:50%;background:var(--navy)}
  .brand-name{color:var(--navy);font-weight:700;font-size:16px;letter-spacing:.6px;text-transform:uppercase}
  .services-title{position:absolute;top:278px;left:0;width:660px;text-align:center;color:var(--white);font-weight:700;font-size:26px}
  .service-list{position:absolute;list-style:none;color:var(--white);font-size:13.6px;line-height:1}
  .service-list li{position:relative;padding-left:22px;margin-bottom:12px}
  .service-list li::before{content:"\2665";position:absolute;left:0;top:-3px;color:var(--green);font-size:18px}
  .service-list.left{left:34px;top:318px;width:300px}
  .service-list.right{left:347px;top:320px;width:300px}
  .service-list li.two-line{line-height:.95}
  .photo{position:absolute;border-radius:50%;border:5px solid var(--white);box-shadow:0 4px 10px rgba(60,50,110,.35)}
  .photo.one{left:122px;top:535px;width:134px;height:134px;background:linear-gradient(135deg,#e2a071,#3a6aa8)}
  .photo.two{left:255px;top:526px;width:152px;height:152px;background:linear-gradient(135deg,#f1e5da,#9fb6cf)}
  .photo.three{left:404px;top:535px;width:134px;height:134px;background:linear-gradient(135deg,#f3ede6,#2f6fc0)}
  .about{position:absolute;top:699px;left:100px;width:460px;text-align:center;color:var(--text-grey);font-weight:300;font-size:14px;line-height:1.12}
  .cta{position:absolute;top:795px;left:19px;color:var(--white);font-weight:700;font-size:16.5px;line-height:1.3}
  .contact{position:absolute;top:786px;left:430px;width:210px;color:var(--white);text-align:left}
  .contact-phone{display:flex;align-items:center;gap:6px;font-size:28px;font-weight:400;line-height:1}
  .contact-line{display:flex;align-items:center;gap:5px;font-size:10.5px;margin-left:40px;margin-top:4px}
  .contact-line svg{flex:none}
</style>
</head>
<body>
<main class="flyer">
  <svg class="flyer-shapes" viewBox="0 0 660 854" aria-hidden="false">
    <defs>
      <linearGradient id="heroFade" x1="0" y1="0" x2="1" y2="0">
        <stop offset="0" stop-color="#f6f6f6"/>
        <stop offset=".5" stop-color="#f1ede9"/>
        <stop offset="1" stop-color="#f4f6f8"/>
      </linearGradient>
      <linearGradient id="bandFill" x1="0" y1="0" x2="0" y2="1">
        <stop offset="0" stop-color="#008479"/>
        <stop offset=".6" stop-color="#0a5d96"/>
        <stop offset="1" stop-color="#0a4d93"/>
      </linearGradient>
      <linearGradient id="footFill" x1="0" y1="0" x2="1" y2="0">
        <stop offset="0" stop-color="#0a4d93"/>
        <stop offset="1" stop-color="#00827a"/>
      </linearGradient>
    </defs>
    <rect x="0" y="0" width="660" height="270" fill="url(#heroFade)" role="img" aria-label="Faded photo of a smiling nurse with an elderly woman"/>
    <path d="M0 262 Q330 222 660 234 L660 244 Q330 232 0 272Z" fill="var(--grey-edge)"/>
    <path d="M0 270 Q330 230 660 242 L660 606 Q600 596 560 600 L100 615 Q40 617 0 618Z" fill="url(#bandFill)"/>
    <path d="M0 618 Q40 617 100 615 L560 600 Q600 596 660 606 L660 612 Q600 602 560 606 L100 621 Q40 623 0 624Z" fill="var(--grey-edge)"/>
    <path d="M0 770 L300 770 Q338 770 362 782 L0 782Z" fill="var(--grey-edge)"/>
    <rect x="0" y="782" width="660" height="72" fill="url(#footFill)"/>
    <path d="M330 782 Q385 800 420 854 L660 854 L660 782Z" fill="var(--white)"/>
    <path d="M348 782 L660 782 L660 854 L432 854 Q400 808 348 782Z" fill="var(--green)"/>
  </svg>

  <h1 class="headline">Seeking Care for Your Loved One?</h1>
  <p class="slogan">Lean On Those Nearby</p>

  <div class="brand">
    <span class="brand-mark"></span>
    <span class="brand-name">Riverbend Trusted Home Care</span>
  </div>

  <h2 class="services-title">Our Services Include</h2>
  <ul class="service-list left">
    <li class="two-line">Experienced Certified Home Health Aides/<br>Live In Home Health Aides/Companions</li>
    <li>Nursing Services</li>
    <li>Alzheimer’s and Dementia Care</li>
    <li>Respite Care</li>
    <li>Postoperative Care</li>
    <li>Post Rehabilitation Care</li>
    <li class="two-line">Assistance with Bathing,<br>Feeding and Grooming</li>
  </ul>
  <ul class="service-list right">
    <li>Running Errands</li>
    <li>Light Housekeeping</li>
    <li>Meal Preparation</li>
    <li>Laundry and Linen Washing</li>
    <li>Mail and Bill Organization</li>
    <li>Medication Management</li>
    <li>Accompanying to Doctor’s Appointments</li>
    <li>And much more!</li>
  </ul>

  <div class="photo one" role="img" aria-label="Photo of a caregiver in scrubs hugging an elderly woman"></div>
  <div class="photo two" role="img" aria-label="Photo of a nurse holding hands with an elderly woman using a cane"></div>
  <div class="photo three" role="img" aria-label="Photo of a nurse in blue scrubs assisting an elderly woman"></div>

  <p class="about">As seasoned professionals, we know how to help our clients navigate and fulfill their various health care needs. Those nearby are here to help you get the attention that you merit.</p>

  <p class="cta">Call Riverbend Trusted Home Care today<br>to learn more about our first-rate services!</p>

  <div class="contact">
    <div class="contact-phone">
      <svg width="24" height="24" viewBox="0 0 24 24" aria-hidden="true"><path d="M6.6 2.5l3 3.6-1.9 2.6c1.3 2.8 3.5 5 6.3 6.4l2.6-1.9 3.6 3-1.5 3.3c-.4.8-1.3 1.2-2.2 1C9 18.8 4.2 14 2.6 6.5c-.2-.9.2-1.8 1-2.2z" fill="#fff"/></svg>
      <span>555-555-555</span>
    </div>
    <div class="contact-line">
      <svg width="13" height="9" viewBox="0 0 13 9" aria-hidden="true"><rect width="13" height="9" fill="#fff"/><path d="M0 0 L6.5 5 L13 0" fill="none" stroke="#8dc63f" stroke-width="1"/></svg>
      <span>Lorem ipsum dolor sit</span>
    </div>
    <div class="contact-line">
      <svg width="12" height="12" viewBox="0 0 12 12" aria-hidden="true"><circle cx="6" cy="6" r="5.5" fill="#fff"/><g fill="none" stroke="#8dc63f" stroke-width=".8"><ellipse cx="6" cy="6" rx="2.5" ry="5.5"/><path d="M.5 6h11M1.5 3h9M1.5 9h9"/></g></svg>
      <span>Lorem ipsum dolor sit</span>
    </div>
  </div>
</main>
</body>
</html>
```